Creative, Innovative PowerPoint Sales Deck Refresh needed

We are a technology firm in the Dallas, TX area and we need the powerpoint presentation used for our sales calls refreshed. This presentation is used in one of the first meetings we have with potential clients, so we want to make a memorable and positive impact - we want something that sets us apart from everyone else. We need 8 master slide templates created for our sales deck and a series of slides within the example sales deck need to be completely refreshed (slides 31-37 and 43 in the sample ppt file) We want a sales deck that is modern, innovative, creative, memorable and whimsical - NOT a typical boring "business" design. Colors should match or compliment the colors used in our logo. The logo in the footer of the attached sample ppt is old - it should be replaced with the newer logo attached. Please take a look at our website to get an idea of our culture and aesthetic www.brightkollow.com
Updates

Project Deadline Extended
Reason: We have received several designs we like and we want our entire team to have time to give them full consideration before making a decision.

Target Market(s)

Business executives

Industry/Entity Type

Information Technology

Font styles to use
Sans Serif

Requirements
Must have
• Our logo and LedgerPeak logo in footer
• Master Slide Templates
• Rework / redesign of slides 31-37 and 43
Nice to have
• We use Raleway font in a lot of our materials

```html
<!DOCTYPE html>
<html lang="en">
<head>
<meta charset="UTF-8">
<title>Phase One Methodology</title>
<link href="https://fonts.googleapis.com/css2?family=Source+Sans+3:wght@300;400;700&display=swap" rel="stylesheet">
<style>
  :root {
    --ink: #1c1c1c;
    --white: #ffffff;
    --bullet-blue: #3f6ab3;
    --step-1: #86c440;
    --step-2: #9bd05e;
    --step-3: #acd77a;
    --step-4: #bde095;
    --step-5: #cde7b2;
    --photo-dark: #2a3440;
    --photo-mid: #8fa4b4;
    --photo-light: #dfe8ee;
    --brand-blue: #1e3f73;
  }
  * { margin: 0; padding: 0; box-sizing: border-box; }
  html, body { width: 1200px; height: 750px; overflow: hidden; background: var(--white); }
  body { font-family: "Source Sans 3", sans-serif; color: var(--ink); }
  .slide { position: relative; width: 1200px; height: 750px; overflow: hidden; background: var(--white); }

  .slide-title {
    position: absolute; left: 51px; top: 58px;
    font-weight: 300; font-size: 55px; line-height: 65px; letter-spacing: -0.5px;
  }

  .hero-photo {
    position: absolute; left: 380px; top: 0; width: 820px; height: 186px;
    border-bottom-left-radius: 150px 186px;
    background:
      linear-gradient(180deg, rgba(255,255,255,0) 55%, rgba(60,80,100,0.55) 80%, rgba(200,215,225,0.9) 100%),
      linear-gradient(90deg, var(--photo-light) 0%, var(--photo-mid) 15%, var(--photo-dark) 30%, var(--photo-mid) 50%, var(--photo-dark) 70%, var(--photo-light) 90%);
  }

  .phase-steps { position: absolute; left: 419px; top: 240px; width: 480px; height: 102px; }

  .task-list { position: absolute; left: 417px; top: 373px; list-style: none; }
  .task-list li {
    position: relative; padding-left: 32px;
    font-size: 18px; font-weight: 400; line-height: 32.7px;
  }
  .task-list li::before {
    content: ""; position: absolute; left: 0; top: 6px;
    width: 20px; height: 20px; border-radius: 50%;
    border: 3px solid var(--bullet-blue);
  }

  .partner-mark {
    position: absolute; display: flex; align-items: center; gap: 12px;
    font-size: 26px; font-weight: 700; color: var(--ink);
  }
  .partner-mark .dot { width: 46px; height: 46px; border-radius: 50%; background: var(--brand-blue); }
  .partner-mark .block { width: 44px; height: 44px; background: var(--brand-blue); }
  .partner-primary { left: 76px; top: 542px; }
  .partner-platform { left: 81px; top: 646px; }
</style>
</head>
<body>
<main class="slide">
  <h1 class="slide-title">Phase One<br>Methodology</h1>

  <div class="hero-photo" role="img" aria-label="Business people standing in a bright meeting room, softly out of focus"></div>

  <svg class="phase-steps" viewBox="0 0 480 102" aria-label="Phase steps">
    <circle cx="401" cy="51" r="50.5" fill="var(--step-5)"/>
    <circle cx="310" cy="51" r="50.5" fill="var(--step-4)"/>
    <circle cx="220" cy="51" r="50.5" fill="var(--step-3)"/>
    <circle cx="129" cy="51" r="50.5" fill="var(--step-2)"/>
    <circle cx="51" cy="51" r="50.5" fill="var(--step-1)"/>
    <text x="51" y="46" text-anchor="middle" fill="var(--white)" font-family="'Source Sans 3', sans-serif" font-weight="700" font-size="17">Project</text>
    <text x="51" y="67" text-anchor="middle" fill="var(--white)" font-family="'Source Sans 3', sans-serif" font-weight="700" font-size="17">initiation</text>
  </svg>

  <ul class="task-list">
    <li>Project Initiation</li>
    <li>Conduct Kickoff Meeting</li>
    <li>Finalize and Publish Project Schedule</li>
    <li>Requirements Definition and Design</li>
    <li>Requirements Traceability Matrix (RTM) Signoff</li>
  </ul>

  <div class="partner-mark partner-primary"><span class="dot"></span>Bright Kollow</div>
  <div class="partner-mark partner-platform"><span class="block"></span>LedgerPeak</div>
</main>
</body>
</html>
```